PPT Template for a company that develops software and intellectual property for use by accountants a

We are a boutique firm that develops specialised reporting applications, financial and non-financial reporting content, checklists and other intellectual property for use by business consultants and accounting firms in particular. The applications and content we are creating is strategically focussed and we are required to produce reports and presentations and our current templates are simply not sufficient.

Excel worksheets, graphs and other graphics are regularly embedded into the presentations
We have our logo in 4 colour palettes and will require the winning version to be provided in all 4 colours plus B&W. There is one single logo but the name “Lantern Trade Pathfinders” is presented in 3 different styles for use depending on the space available etc.
Our clients will typically take our products and rebrand/co brand these (we require them to at least say that there product is “powered by Lantern Trade Pathfinders” with the logo.
The templates you provide will be used to create marketing presentations, proposal presentations and our standard documents that clients will rebrand or cobrand under license.

A Powerpoint Document Slide Template

Cover page layout, back page, intermediate page heading, in colours and styles based on the logo, title styles, and an intermediate or chapter heading slide style. Many of our presentations contain slides with tables, diagrams, flowcharts and text, including simple lists of bullet points. As above, you will see in our style guide that we have four coloured logos – we would like one version in each. We recommend that we finalise the design using the maroon version and then this be used as the base for the other colour palettes.
Again, the cover should be bold and draw attention but remain professional.

We are looking for something that works in both 4:3 and 16:9 (or two templates please)

We like a clear professional and simple look.

Deliverable: PowerPoint template file (.potx extension) for PowerPoint 2007 with at least a “cover” layout, a “title and content” layout, and a simplified slide layout, as well as “back cover”. Please embed any fonts used.

Industry/Entity Type

Financial

```html
<!DOCTYPE html>
<html lang="en">
<head>
<meta charset="utf-8">
<title>Lantern Trade Pathfinders – Presentation Template</title>
<link href="https://fonts.googleapis.com/css2?family=Roboto:ital,wght@0,300;0,400;0,500;1,400&display=swap" rel="stylesheet">
<style>
:root{
  --red:#b01c22;
  --red-soft:#c0393e;
  --charcoal:#3d3d3f;
  --grey:#8e8e90;
  --grey-light:#a9a9ab;
  --text:#7a7a7a;
  --board:#cacaca;
  --white:#ffffff;
}
*{margin:0;padding:0;box-sizing:border-box}
html,body{width:1200px;height:946px;overflow:hidden}
body{background:var(--board);font-family:'Roboto',Arial,sans-serif;color:var(--text);position:relative}
.slide{position:absolute;width:377px;height:292px;background:var(--white);overflow:hidden}
.r1{top:32px}.r2{top:334px}.r3{top:636px}
.c1{left:24px}.c2{left:412px}.c3{left:801px}
.abs{position:absolute}
.title{position:absolute;left:21px;top:18px;font-size:14px;font-weight:300;color:var(--red);letter-spacing:.2px}
.title-rule{position:absolute;left:21px;right:20px;top:33px;height:1px;background:#9a9a9a}
.footer{position:absolute;left:0;bottom:0;width:377px;height:10px}
.brand{position:absolute;font-weight:500;color:var(--charcoal);line-height:1.05}
.brand.small{left:8px;bottom:13px;font-size:5.5px}
.brand.white{color:var(--white)}
.copy{font-size:5px;line-height:8px;color:var(--text);text-align:justify}
.photo{position:absolute;background:linear-gradient(135deg,#e9e9e9,#9d9d9d 55%,#4a4a4a)}
/* cover */
.cover-head{left:37px;top:111px;color:var(--white);font-size:16px;font-weight:300;line-height:20px}
.cover-date{left:37px;top:157px;color:var(--white);font-size:8px;font-weight:300}
.cover-brand{right:30px;top:242px;font-size:11px}
/* about */
.about-lead{left:21px;top:146px;width:108px;font-size:5.6px;line-height:10px;color:var(--red)}
.about-body{left:139px;top:146px;width:218px}
.about-body p{margin-bottom:12px;font-size:5.6px;line-height:9.6px}
.band{left:0;top:53px;width:377px;height:77px;background:var(--charcoal)}
.band-text{left:157px;top:61px;width:200px;color:var(--white);font-size:6.2px;line-height:13px;font-style:italic;text-align:justify}
.about2-body{left:157px;top:138px;width:200px}
.about2-body p{margin-bottom:8px;font-size:4.8px;line-height:7.5px}
/* chart */
.legend{position:absolute;top:229px;width:84px}
.legend b{display:block;font-weight:400;font-size:5.5px;color:var(--charcoal);margin-bottom:2px}
.legend b i{display:inline-block;width:5px;height:5px;margin-right:3px;vertical-align:-.5px}
.legend p{font-size:4.2px;line-height:6px;margin-left:8px;text-align:justify}
/* services / team */
.col{position:absolute;width:100px;text-align:center}
.col h3{font-size:8.5px;font-weight:500;color:var(--red);margin-bottom:3px}
.col p{font-size:4.6px;line-height:7.4px;color:#a3a3a3}
.team-intro{left:30px;top:55px;width:317px;text-align:center;font-size:5.3px;line-height:10px;font-style:italic;color:#555}
.member{position:absolute;width:82px;text-align:center}
.member h4{font-size:6.2px;font-weight:400;color:var(--red)}
.member small{display:block;font-size:4.6px;font-style:italic;color:#555;margin-bottom:8px}
.member p{font-size:5px;line-height:10.5px;color:#a3a3a3;text-align:justify}
.portrait{position:absolute;width:58px;height:58px;border-radius:50%;border:1.5px solid var(--red);background:radial-gradient(circle at 50% 40%,#efefef,#8c8c8c)}
/* image text */
.panel{left:0;top:0;width:185px;height:292px;background:var(--red)}
.panel-title{left:13px;top:20px;font-size:13px;font-weight:300;color:var(--white)}
.panel-lead{left:23px;top:103px;font-size:5.2px;color:var(--white)}
.panel-body{left:23px;top:113px;width:150px}
.panel-body p{font-size:4.9px;line-height:7.5px;color:var(--white);text-align:justify;margin-bottom:7px}
/* section */
.section{background:var(--red)}
.section-label{left:0;width:377px;top:195px;text-align:center;color:var(--white);font-size:13px;font-weight:300}
/* back */
.back-brand{left:69px;top:47px;font-size:11px}
.thanks{left:30px;top:154px;color:var(--white);font-size:13px;font-weight:300}
.thanks-sub{left:30px;top:172px;color:var(--white);font-size:5.5px}
.contact{left:30px;font-size:5.8px;line-height:7px;color:var(--white);display:flex;gap:5px;align-items:flex-start}
.contact svg{flex:none;margin-top:.5px}
</style>
</head>
<body>

<!-- Cover -->
<section class="slide r1 c1">
  <svg class="abs" width="377" height="292" viewBox="0 0 377 292">
    <defs><linearGradient id="coverShade" x1="0" x2="1"><stop offset="0" stop-color="#b01c22"/><stop offset="1" stop-color="#c2474b"/></linearGradient></defs>
    <path d="M0 93 H152 C172 93 176 68 205 68 H377 V190 H0 Z" fill="url(#coverShade)"/>
    <rect x="0" y="192" width="377" height="2" fill="#3d3d3f"/>
    <rect x="0" y="284" width="377" height="8" fill="#b01c22"/>
  </svg>
  <div class="abs cover-head">WELCOME<br>TO OUR PRESENTATION</div>
  <div class="abs cover-date">Birmingham, March 25, 2011</div>
  <div class="brand cover-brand">Lantern Trade<br>Pathfinders</div>
</section>

<!-- About us 1 -->
<section class="slide r1 c2">
  <div class="title">ABOUT US</div><div class="title-rule"></div>
  <div class="photo" style="left:21px;top:46px;width:336px;height:81px" role="img" aria-label="Black and white photo of a smiling business team"></div>
  <div class="abs about-lead">LOREM IPSUM DOLOR SIT MET CONSECTETUR ADIPISCING ELIT, SED DO EIUSMOD TEMPOR INCIDIDUNT UT LABORE ET DELORE MAGNA</div>
  <div class="abs about-body copy">
    <p>Lorem ipsum dolor sit amet, consectetur adipisicing elit, sed do eiusmod tempor incididunt ut labore et dolore magna aliqua. Ut enim ad minim veniam, quis nostrud exercitation ullamco laboris nisi ut aliquip ex ea commodo consequat. Duis aute irure dolor in reprehenderit in voluptate velit esse cillum dolore eu fugiat nulla pariatur.</p>
    <p>Lorem ipsum dolor sit amet, consectetur adipisicing elit, sed do eiusmod tempor incididunt ut labore et dolore magna aliqua. Ut enim ad minim veniam, quis nostrud exercitation ullamco laboris nisi ut aliquip ex ea commodo consequat. Duis aute irure dolor in reprehenderit in voluptate velit esse cillum dolore eu</p>
  </div>
  <div class="brand small">Lantern Trade<br>Pathfinders</div>
  <svg class="footer" viewBox="0 0 377 10"><rect x="0" y="7" width="377" height="3" fill="#3d3d3f"/><path d="M290 10 L300 3 H377 V10 Z" fill="#b01c22"/><text x="367" y="8.5" font-size="4" fill="#fff">1</text></svg>
</section>

<!-- About us 2 -->
<section class="slide r1 c3">
  <div class="title">ABOUT US</div><div class="title-rule"></div>
  <div class="abs band"></div>
  <div class="photo" style="left:20px;top:53px;width:114px;height:88px" role="img" aria-label="Black and white photo of a businesswoman"></div>
  <div class="abs band-text">Lorem ipsum dolor sit amet consectetur adipisicing elit, sed do eiusmod tempor incididunt ut labore et dolore magna aliqua. Ut enim ad</div>
  <div class="abs about2-body copy">
    <p>Lorem ipsum dolor sit amet, consectetur adipisicing elit, sed do eiusmod tempor incididunt ut labore et dolore magna aliqua. Ut enim ad minim veniam, quis nostrud exercitation ullamco laboris nisi ut aliquip ex ea commodo consequat. Duis aute irure dolor in reprehenderit in voluptate velit esse cillum dolore eu fugiat nulla pariatur.</p>
    <p>Lorem ipsum dolor sit amet, consectetur adipisicing elit, sed do eiusmod tempor incididunt ut labore et dolore magna aliqua. Ut enim ad minim veniam, quis nostrud exercitation ullamco laboris nisi ut aliquip ex ea commodo consequat. Duis aute irure dolor in reprehenderit in voluptate velit esse cillum dolore eu</p>
    <p>fugiat nulla pariatur. Excepteur sint occaecat cupidatat non proident, sunt in culpa qui officia deserunt mollit anim id est laborum. Excepteur sint occaecat cupidatat non proident, sunt in consequat. Duis aute irure dolor in reprehenderit</p>
  </div>
  <div class="brand small">Lantern Trade<br>Pathfinders</div>
  <svg class="footer" viewBox="0 0 377 10"><rect x="0" y="7" width="377" height="3" fill="#3d3d3f"/><path d="M290 10 L300 3 H377 V10 Z" fill="#b01c22"/><text x="367" y="8.5" font-size="4" fill="#fff">1</text></svg>
</section>

<!-- Chart -->
<section class="slide r2 c1">
  <div class="title">OUR CHART</div><div class="title-rule"></div>
  <svg class="abs" style="left:0;top:0" width="377" height="220" viewBox="0 0 377 220" font-family="Roboto, Arial, sans-serif">
    <g stroke="#555" stroke-width=".7">
      <line x1="71" y1="59" x2="71" y2="190"/><line x1="71" y1="190" x2="298" y2="190"/>
      <line x1="68" y1="81" x2="71" y2="81"/><line x1="68" y1="103" x2="71" y2="103"/><line x1="68" y1="125" x2="71" y2="125"/><line x1="68" y1="147" x2="71" y2="147"/><line x1="68" y1="168" x2="71" y2="168"/>
    </g>
    <g>
      <rect x="80.5" y="95" width="13.5" height="95" fill="#b01c22"/><rect x="94" y="137" width="13.5" height="53" fill="#8e8e90"/><rect x="107.5" y="146.5" width="13" height="43.5" fill="#3d3d3f"/>
      <rect x="137" y="121" width="13.5" height="69" fill="#b01c22"/><rect x="150.5" y="95" width="13.5" height="95" fill="#8e8e90"/><rect x="164" y="146.5" width="13" height="43.5" fill="#3d3d3f"/>
      <rect x="194" y="104" width="13.5" height="86" fill="#b01c22"/><rect x="207.5" y="148" width="13.5" height="42" fill="#8e8e90"/><rect x="221" y="130" width="13" height="60" fill="#3d3d3f"/>
      <rect x="250" y="107.5" width="13.5" height="82.5" fill="#b01c22"/><rect x="263.5" y="139" width="13.5" height="51" fill="#8e8e90"/><rect x="277" y="98" width="13" height="92" fill="#3d3d3f"/>
    </g>
    <g font-size="9" fill="#444" text-anchor="middle">
      <text x="101" y="209">2009</text><text x="157" y="209">2010</text><text x="214" y="209">2011</text><text x="270" y="209">2012</text>
    </g>
  </svg>
  <div class="legend" style="left:51px"><b><i style="background:var(--red)"></i>LOREM IPSUM</b><p>Lorem ipsum dolor sit amet, consectetur adipisicing elit, sed do eiusmod tempor incididunt ut labore et dolore magna</p></div>
  <div class="legend" style="left:156px"><b><i style="background:var(--grey)"></i>LOREM IPSUM</b><p>Lorem ipsum dolor sit amet, consectetur adipisicing elit, sed do eiusmod tempor incididunt ut labore et dolore magna</p></div>
  <div class="legend" style="left:258px"><b><i style="background:var(--charcoal)"></i>LOREM IPSUM</b><p>Lorem ipsum dolor sit amet, consectetur adipisicing elit, sed do eiusmod tempor incididunt ut labore et dolore magna</p></div>
  <div class="brand small">Lantern Trade<br>Pathfinders</div>
  <svg class="footer" viewBox="0 0 377 10"><rect x="0" y="7" width="377" height="3" fill="#3d3d3f"/><path d="M290 10 L300 3 H377 V10 Z" fill="#b01c22"/><text x="367" y="8.5" font-size="4" fill="#fff">1</text></svg>
</section>

<!-- Services -->
<section class="slide r2 c2">
  <div class="title">OUR SERVICES</div><div class="title-rule"></div>
  <svg class="abs" style="left:0;top:0" width="377" height="140" viewBox="0 0 377 140">
    <circle cx="76" cy="110" r="22" fill="#3d3d3f"/>
    <circle cx="76" cy="110" r="7.5" fill="none" stroke="#fff" stroke-width="4" stroke-dasharray="3 2.9"/>
    <circle cx="76" cy="110" r="5" fill="#fff"/><circle cx="76" cy="110" r="2.2" fill="#3d3d3f"/>
    <circle cx="188" cy="110" r="22" fill="#b01c22"/>
    <g fill="#fff"><rect x="179" y="110" width="4" height="9"/><rect x="185" y="106" width="4" height="13"/><rect x="191" y="102" width="4" height="17"/></g>
    <path d="M178 106 L186 100 L190 103 L197 97" stroke="#fff" stroke-width="1.6" fill="none"/><path d="M194 96 H198 V100 Z" fill="#fff"/>
    <circle cx="310" cy="110" r="22" fill="#a9a9ab"/>
    <g stroke="#fff" stroke-width="1.5" fill="none"><rect x="300" y="101" width="20" height="13"/><line x1="298" y1="101" x2="322" y2="101"/><line x1="310" y1="114" x2="310" y2="119"/><line x1="305" y1="121" x2="310" y2="114"/><line x1="315" y1="121" x2="310" y2="114"/></g>
  </svg>
  <div class="col" style="left:26px;top:147px"><h3>OUR SERVICES</h3><p>dolor sit amet, consectetur adipisicing elit, sed do eiusmod tempor incididunt ut labore et dolore magna aliqua. Ut enim ad minim veniam, quis nostrud exercitation ullamco laboris nisi ut aliquip ex ea cesse cillum dolore eu fugiat nulla pariatur.</p></div>
  <div class="col" style="left:138px;top:147px"><h3>OUR SERVICES</h3><p>dolor sit amet, consectetur adipisicing elit, sed do eiusmod tempor incididunt ut labore et dolore magna aliqua. Ut enim ad minim veniam, quis nostrud exercitation ullamco laboris nisi ut aliquip ex ea cesse cillum dolore eu fugiat nulla pariatur.</p></div>
  <div class="col" style="left:260px;top:147px"><h3>OUR SERVICES</h3><p>dolor sit amet, consectetur adipisicing elit, sed do eiusmod tempor incididunt ut labore et dolore magna aliqua. Ut enim ad minim veniam, quis nostrud exercitation ullamco laboris nisi ut aliquip ex ea cesse cillum dolore eu fugiat nulla pariatur.</p></div>
  <div class="brand small">Lantern Trade<br>Pathfinders</div>
  <svg class="footer" viewBox="0 0 377 10"><rect x="0" y="7" width="377" height="3" fill="#3d3d3f"/><path d="M290 10 L300 3 H377 V10 Z" fill="#b01c22"/><text x="367" y="8.5" font-size="4" fill="#fff">1</text></svg>
</section>

<!-- Team -->
<section class="slide r2 c3">
  <div class="title">OUR TEAM</div><div class="title-rule"></div>
  <div class="abs team-intro">dolor sit amet, consectetur adipisicing elit, sed do eiusmod tempor incididunt ut labore et dolore magna aliqua.<br>Ut enim ad minim veniam, quis nostrud exercitation ullamco laboris nisi ut a</div>
  <div class="portrait" style="left:54px;top:90px" role="img" aria-label="Portrait photo of Jonathan Doe"></div>
  <div class="portrait" style="left:162px;top:90px" role="img" aria-label="Portrait photo of Melanie Doe"></div>
  <div class="portrait" style="left:268px;top:90px" role="img" aria-label="Portrait photo of Natalie Doe"></div>
  <div class="member" style="left:42px;top:156px"><h4>JONATHAN DOE</h4><small>President</small><p>dolor sit amet, consectetur adipisicing elit, sed do eiusmod tempor incididunt ut labore et dolore magna aliqua. Ut enim ad minim veniam, quis nostrud exercitation</p></div>
  <div class="member" style="left:150px;top:156px"><h4>MELANIE DOE</h4><small>CEO / Founder</small><p>dolor sit amet, consectetur adipisicing elit, sed do eiusmod tempor incididunt ut labore et dolore magna aliqua. Ut enim ad minim veniam, quis nostrud exercitation</p></div>
  <div class="member" style="left:256px;top:156px"><h4>NATALIE DOE</h4><small>Vice President</small><p>dolor sit amet, consectetur adipisicing elit, sed do eiusmod tempor incididunt ut labore et dolore magna aliqua. Ut enim ad minim veniam, quis nostrud exercitation</p></div>
  <div class="brand small">Lantern Trade<br>Pathfinders</div>
  <svg class="footer" viewBox="0 0 377 10"><rect x="0" y="7" width="377" height="3" fill="#3d3d3f"/><path d="M290 10 L300 3 H377 V10 Z" fill="#b01c22"/><text x="367" y="8.5" font-size="4" fill="#fff">1</text></svg>
</section>

<!-- Image text -->
<section class="slide r3 c1">
  <div class="abs panel"></div>
  <div class="photo" style="left:185px;top:0;width:192px;height:292px" role="img" aria-label="Black and white photo of two smiling business professionals"></div>
  <div class="abs panel-title">IMAGE TEXT</div>
  <div class="abs panel-lead">LOREM IPSUM DOLOR SIT MET</div>
  <div class="abs panel-body">
    <p>Lorem ipsum dolor sit amet, consectetur adipisicing elit, sed do eiusmod tempor incididunt ut labore et dolore magna aliqua. Ut enim ad minim veniam, quis nostrud exercitation ullamco laboris nisi ut aliquip ex ea commodo consequat. Duis aute irure dolor in reprehenderit in voluptate velit esse cillum dolore eu fugiat nulla pariatur.</p>
    <p>Lorem ipsum dolor sit amet, consectetur adipisicing elit, sed do eiusmod tempor incididunt ut labore et dolore magna aliqua. Ut enim ad minim veniam, quis nostrud exercitation ullamco laboris nisi ut aliquip ex ea commodo consequat. Duis aute irure dolor in reprehenderit in voluptate velit esse cillum dolore eu</p>
  </div>
  <div class="brand small white">Lantern Trade<br>Pathfinders</div>
</section>

<!-- Section title -->
<section class="slide r3 c2 section">
  <svg class="abs" width="377" height="292" viewBox="0 0 377 292">
    <circle cx="188" cy="151" r="24" fill="#fff"/>
    <circle cx="190" cy="139" r="3.6" fill="#b01c22"/>
    <path d="M183 147 H193 L189 163 H193 L192 166 H181 L182 163 H185 L188 150 H182 Z" fill="#b01c22"/>
    <rect x="135" y="182.5" width="108" height="1" fill="#fff"/>
  </svg>
  <div class="abs section-label">SECTION TITLE</div>
</section>

<!-- Back cover -->
<section class="slide r3 c3">
  <div class="brand back-brand">Lantern Trade<br>Pathfinders</div>
  <svg class="abs" width="377" height="292" viewBox="0 0 377 292">
    <defs><linearGradient id="backShade" x1="0" x2="1"><stop offset="0" stop-color="#b01c22"/><stop offset="1" stop-color="#c2474b"/></linearGradient></defs>
    <path d="M0 113 H168 C186 113 190 87 214 87 H377 V287 H0 Z" fill="url(#backShade)"/>
    <rect x="0" y="287" width="377" height="5" fill="#3d3d3f"/>
  </svg>
  <div class="abs thanks">THANK YOU</div>
  <div class="abs thanks-sub">FOR YOUR TIME</div>
  <div class="abs contact" style="top:207px"><svg width="7" height="7" viewBox="0 0 10 10"><circle cx="5" cy="5" r="5" fill="#fff"/><path d="M5 2a2 2 0 0 1 2 2c0 1.5-2 4-2 4S3 5.5 3 4a2 2 0 0 1 2-2z" fill="#b01c22"/></svg><span>4120 Harbor Lane Ste 300<br>Fairview, Ohio 45011</span></div>
  <div class="abs contact" style="top:230px"><svg width="7" height="7" viewBox="0 0 10 10"><circle cx="5" cy="5" r="5" fill="#fff"/><path d="M3 3h1.3l.6 1.4-.8.6a4 4 0 0 0 1.9 1.9l.6-.8 1.4.6V8C5 8 2 5 3 3z" fill="#b01c22"/></svg><span>1.800.555.0142</span></div>
  <div class="abs contact" style="top:246px"><svg width="7" height="7" viewBox="0 0 10 10"><circle cx="5" cy="5" r="5" fill="#fff"/><rect x="2.5" y="3.3" width="5" height="3.6" fill="#b01c22"/><path d="M2.5 3.3 5 5.3 7.5 3.3" stroke="#fff" stroke-width=".5" fill="none"/></svg><span>support@lanternpathfinders.com</span></div>
  <div class="abs contact" style="top:262px"><svg width="7" height="7" viewBox="0 0 10 10"><circle cx="5" cy="5" r="5" fill="#fff"/><circle cx="5" cy="5" r="2.8" fill="none" stroke="#b01c22" stroke-width=".7"/><line x1="2.2" y1="5" x2="7.8" y2="5" stroke="#b01c22" stroke-width=".6"/><ellipse cx="5" cy="5" rx="1.2" ry="2.8" fill="none" stroke="#b01c22" stroke-width=".6"/></svg><span>www.lanternpathfinders.com</span></div>
</section>

</body>
</html>
```